DORIVAN
POWER THE FUTURE
Professional
Tobin Rasquelle
2417 Fennimore Lane
Harlow Springs, VA 22419
tobin@dorivan7.com
www.dorivan7.com
I can provide logo as need it.
Logo and write this underneath the logo or where you think it will look better.
Have fun!!

```html
<!DOCTYPE html>
<html lang="en">
<head>
<meta charset="utf-8">
<title>DORIVAN Business Card</title>
<link href="https://fonts.googleapis.com/css2?family=Open+Sans:wght@400;600;700;800&display=swap" rel="stylesheet">
<style>
  :root {
    --bg: #e9ebee;
    --brand-blue: #1976c8;
    --brand-blue-dark: #1565b0;
    --accent-green: #3aa935;
    --ink: #1f2a36;
    --muted: #4a5663;
    --white: #ffffff;
  }
  * { box-sizing: border-box; margin: 0; padding: 0; }
  html, body {
    width: 1200px; height: 770px; overflow: hidden;
    background: var(--bg);
    font-family: "Open Sans", Arial, sans-serif;
  }
  .stage {
    position: relative; width: 1200px; height: 770px;
    display: flex; align-items: center; justify-content: center; gap: 50px;
  }
  .card {
    position: relative; width: 540px; height: 309px;
    border-radius: 22px; overflow: hidden;
    box-shadow: 0 10px 30px rgba(0,0,0,0.18);
  }
  /* Front */
  .card-front { background: var(--white); }
  .card-front .band { position: absolute; left: 0; top: 0; width: 540px; height: 309px; }
  .brand-name {
    position: absolute; left: 34px; top: 30px;
    font-weight: 800; font-size: 50px; letter-spacing: 1px;
    color: var(--brand-blue); line-height: 1;
  }
  .person-name {
    position: absolute; left: 36px; top: 106px;
    font-weight: 700; font-size: 15px; color: var(--ink);
  }
  .web-left {
    position: absolute; left: 36px; top: 186px;
    font-size: 11px; color: var(--muted);
  }
  .contact-list {
    position: absolute; left: 318px; top: 138px;
    list-style: none; font-size: 11px; color: var(--muted); line-height: 1.35;
  }
  .contact-list li { display: flex; gap: 8px; margin-bottom: 5px; align-items: flex-start; }
  .contact-list svg { flex: none; margin-top: 2px; }
  .toll-free {
    position: absolute; right: 30px; bottom: 22px;
    display: flex; align-items: center; gap: 10px; color: var(--white);
  }
  .toll-free .label {
    font-size: 10px; font-weight: 700; line-height: 1.15; text-transform: uppercase; text-align: right;
  }
  .toll-free .number { font-size: 27px; font-weight: 800; letter-spacing: 0.5px; }
  /* Back */
  .card-back {
    background: var(--brand-blue);
    display: flex; flex-direction: column; align-items: center; justify-content: center;
  }
  .card-back .brand-name {
    position: static; color: var(--white); font-size: 58px;
  }
  .card-back .web-back {
    margin-top: 22px; font-size: 11px; color: var(--white); opacity: 0.9;
  }
</style>
</head>
<body>
<main class="stage">
  <section class="card card-front" aria-label="Business card front">
    <svg class="band" viewBox="0 0 540 309" aria-hidden="true">
      <path d="M0 222 C 160 230, 360 232, 540 262 L540 309 L0 309 Z" fill="var(--brand-blue)"/>
      <path d="M0 218 C 160 226, 360 228, 540 258" fill="none" stroke="var(--accent-green)" stroke-width="4"/>
    </svg>
    <div class="brand-name">DORIVAN</div>
    <div class="person-name">Tobin Rasquelle</div>
    <div class="web-left">www.dorivan7.com</div>
    <ul class="contact-list">
      <li>
        <svg width="10" height="12" viewBox="0 0 10 12"><path d="M5 0a4 4 0 0 1 4 4c0 3-4 8-4 8S1 7 1 4a4 4 0 0 1 4-4z" fill="var(--brand-blue)"/><circle cx="5" cy="4" r="1.5" fill="#fff"/></svg>
        <span>2417 Fennimore Lane<br>Harlow Springs, VA 22419</span>
      </li>
      <li>
        <svg width="10" height="12" viewBox="0 0 10 12"><rect x="0" y="2" width="10" height="8" rx="1" fill="var(--brand-blue)"/><path d="M0 3l5 4 5-4" fill="none" stroke="#fff" stroke-width="1"/></svg>
        <span>tobin@dorivan7.com<br>703-615-2048<br>703-615-2097</span>
      </li>
    </ul>
    <div class="toll-free">
      <span class="label">Call us<br>toll free</span>
      <span class="number">1-800-482-5530</span>
    </div>
  </section>

  <section class="card card-back" aria-label="Business card back">
    <div class="brand-name">DORIVAN</div>
    <div class="web-back">www.dorivan7.com</div>
  </section>
</main>
</body>
</html>
```